International Honeymoon Tour Operator needs Business Card

We need to design a business card including our new logo for a new tour operator called Marisol Thorne Getaways. We would like to also include the text 'Personal Tailor-Made Honeymoons for our Guests at a Lower Cost'. Please Include the following details as well; 'Website: www.marisolthornegetaways.co.uk'; 'E-mail: felix@marisolthornegetaways.co.uk'; 'Mobile: 07914263058'. We would like the design to be compatible with the logo and text. The final design should communicate professionalism, modern and ethical.

We want to business card to be double sided.

We would like to be able to easily adjust the e-mail address and contact number in the future for other employees either through you or ourselves.

Target Market(s)

Brides and grooms aged 18-35 predominantly.

Industry/Entity Type

Business

Colors

Designer to choose colors to be used in the design.

Requirements
Must have
• Logo
Requested Text
Double sided
Nice to have
• Additional colour
The wow factor
Should not have
• Images of currency

```html
<!DOCTYPE html>
<html lang="en">
<head>
<meta charset="utf-8">
<title>Marisol Thorne Getaways – Business Card</title>
<link rel="stylesheet" href="https://fonts.googleapis.com/css2?family=Jost:wght@400;500;600&display=swap">
<style>
  :root {
    --backdrop: #8a8786;
    --card-teal: #5f8a7e;
    --teal-deep: #3e6660;
    --leaf-green: #8cc63f;
    --paper: #f7f7f5;
    --ink-grey: #6a6a6a;
    --white: #ffffff;
  }
  * { margin: 0; padding: 0; box-sizing: border-box; }
  html, body {
    width: 1200px; height: 799px; overflow: hidden;
    background: var(--backdrop);
    font-family: "Jost", sans-serif;
  }
  .canvas { position: relative; width: 1200px; height: 799px; }
  .card {
    position: absolute; left: 385px;
    width: 430px; height: 266px;
  }
  .card--front { top: 82px; background: var(--card-teal); }
  .card--back { top: 446px; background: var(--paper); }

  .front-brand {
    position: absolute; left: 0; right: 0; top: 112px;
    text-align: center;
    color: var(--teal-deep);
    font-weight: 400; font-size: 27px; letter-spacing: 0.5px;
  }
  .tagline {
    position: absolute; left: 0; right: 0; top: 203px;
    text-align: center;
    color: var(--white);
    font-weight: 500; font-size: 9.6px; letter-spacing: 0.6px;
    text-transform: uppercase;
  }

  .back-brand {
    position: absolute; right: 32px; top: 42px;
    display: flex; align-items: center; gap: 8px;
    color: var(--teal-deep);
    font-weight: 400; font-size: 19px;
  }
  .back-brand .mark {
    width: 12px; height: 12px; border-radius: 50%;
    background: var(--leaf-green);
  }
  .person { position: absolute; left: 35px; top: 153px; }
  .person__name {
    color: var(--teal-deep);
    font-weight: 600; font-size: 11.5px; letter-spacing: 1px;
  }
  .person__role {
    color: var(--leaf-green);
    font-weight: 500; font-size: 8px; letter-spacing: 0.6px;
    margin-top: 2px;
  }
  .contact {
    position: absolute; left: 35px; top: 195px;
    list-style: none;
    color: var(--ink-grey);
    font-weight: 400; font-size: 7.4px; letter-spacing: 0.4px;
    text-transform: uppercase; line-height: 15px;
  }
</style>
</head>
<body>
<main class="canvas">
  <section class="card card--front" aria-label="Card front">
    <p class="front-brand">Marisol Thorne Getaways</p>
    <p class="tagline">Personal tailor-made honeymoons for our guests at a lower cost</p>
  </section>

  <section class="card card--back" aria-label="Card back">
    <p class="back-brand"><span class="mark"></span>Marisol Thorne Getaways</p>
    <div class="person">
      <p class="person__name">JHON DOE</p>
      <p class="person__role">CEO</p>
    </div>
    <ul class="contact">
      <li>www.marisolthornegetaways.co.uk</li>
      <li>felix@marisolthornegetaways.co.uk</li>
      <li>07914263058</li>
    </ul>
  </section>
</main>
</body>
</html>
```